Portrait of a Graduate

Our school community has created a document which describes the characteristics that every student who graduates from our school should possess. We would like a visual graphic to present the information to parents\ community. We came up with three buckets (Personal, Social, and Academic) and the concept "BLH Graduates Will Be Okay" is the central theme.
We are open to 2 different concepts:
1. A ven diagram of sorts, where the three buckets are each in an area - and the over lap is "BLH Graduates Will Be Okay"
2. Our logo has a sassafras leaf in it - using the leaves to represent each bucket and the central concept as the stem - or some other creative version.

The text to be used is below:

BLH Graduates Will Be Okay (at the center/on the stem)

1. Personal
They will:
have self-worth
advocate for themselves
feel secure in their future

2. Social
They will:
embrace differences
engage in trusting relationships
be compassionate (members of their community)

3. Academic
They will:
apply skills and strategies
creatively problem-solve
achieve individual success

```html
<!DOCTYPE html>
<html lang="en">
<head>
<meta charset="utf-8">
<title>Portrait of a Graduate – Briar Lane Hall</title>
<link href="https://fonts.googleapis.com/css2?family=Lora:ital,wght@0,500;0,700;1,700&family=Libre+Baskerville:wght@700&display=swap" rel="stylesheet">
<style>
  :root {
    --navy: #152c48;
    --gold: #c8a92e;
    --paper-top: #ebeaed;
    --paper-body: #dcdbdf;
    --stage: #e4e4e7;
    --ink: #14263d;
  }
  * { box-sizing: border-box; margin: 0; padding: 0; }
  html, body {
    width: 1180px; height: 1200px; overflow: hidden;
    background: var(--stage);
  }
  .sheet {
    position: absolute; left: 133px; top: 0;
    width: 914px; height: 1200px;
    background: var(--paper-body);
    overflow: hidden;
  }
  .sheet__band-top {
    position: absolute; left: 0; top: 0; width: 100%; height: 23px;
    background: var(--gold);
  }
  .sheet__header {
    position: absolute; left: 0; top: 23px; width: 100%; height: 245px;
    background: var(--paper-top);
  }
  .sheet__footer-strip {
    position: absolute; left: 0; top: 1127px; width: 100%; height: 19px;
    background: var(--paper-top);
  }
  .sheet__band-bottom {
    position: absolute; left: 0; top: 1146px; width: 100%; height: 54px;
    background: var(--navy);
  }
  .brand {
    position: absolute; left: 91px; top: 100px;
    font-family: "Lora", serif; font-weight: 500;
    font-size: 50px; line-height: 1; color: var(--navy);
    letter-spacing: 0.5px;
  }
  .diagram { position: absolute; left: 0; top: 0; width: 914px; height: 1200px; }
  .hub {
    position: absolute; left: 348px; top: 587px;
    width: 222px; height: 222px; border-radius: 50%;
    background: var(--gold);
    border: 4px solid #ecebee;
    display: flex; align-items: center; justify-content: center;
    text-align: center;
    font-family: "Lora", serif; font-weight: 700;
    font-size: 31px; line-height: 1.16; color: var(--navy);
  }
  .bucket { position: absolute; }
  .bucket__title {
    font-family: "Lora", serif; font-style: italic; font-weight: 700;
    font-size: 45px; line-height: 1; color: var(--navy);
    margin-bottom: 16px;
  }
  .bucket__list { list-style: none; }
  .bucket__item {
    position: relative; padding-left: 22px;
    font-family: "Libre Baskerville", serif; font-weight: 700;
    font-size: 13.5px; letter-spacing: 0.3px; text-transform: uppercase;
    color: var(--ink); line-height: 1.2; margin-bottom: 16px;
  }
  .bucket__item svg { position: absolute; left: 0; top: 1px; width: 15px; height: 13px; }
  .bucket__note { display: block; font-size: 11.5px; font-weight: 700; letter-spacing: 0.2px; }
  .bucket--personal { left: 586px; top: 400px; }
  .bucket--personal .bucket__item { margin-bottom: 14px; }
  .bucket--social { left: 114px; top: 846px; }
  .bucket--academic { left: 590px; top: 846px; }
  .bucket--academic .bucket__title { margin-left: -4px; }
</style>
</head>
<body>
<main class="sheet">
  <div class="sheet__band-top"></div>
  <header class="sheet__header">
    <div class="brand">Briar Lane Hall</div>
  </header>

  <svg class="diagram" viewBox="0 0 914 1200">
    <defs>
      <linearGradient id="leafTone" x1="0" y1="0" x2="1" y2="1">
        <stop offset="0" stop-color="#1b3556"/>
        <stop offset="1" stop-color="#12273f"/>
      </linearGradient>
    </defs>
    <g class="leaf-art" role="img" aria-label="Illustration of three sassafras leaves radiating from the centre" fill="url(#leafTone)">
      <rect x="296" y="400" width="175" height="230" rx="70"/>
      <rect x="109" y="585" width="694" height="205" rx="95"/>
      <rect x="505" y="780" width="40" height="75" rx="18"/>
    </g>
    <g class="connectors" fill="none" stroke="var(--navy)" stroke-width="2.5" stroke-dasharray="5 5">
      <polyline points="555,423 459,423 426,452"/>
      <polyline points="74,855 74,798 173,760"/>
      <polyline points="815,856 815,797 759,777"/>
    </g>
    <g class="connector-dots" fill="var(--gold)">
      <circle cx="557" cy="423" r="9"/>
      <circle cx="74" cy="870" r="9"/>
      <circle cx="815" cy="871" r="9"/>
    </g>
  </svg>

  <div class="hub">BLH<br>Graduates<br>Will Be<br>Okay</div>

  <section class="bucket bucket--personal">
    <h2 class="bucket__title">Personal</h2>
    <ul class="bucket__list">
      <li class="bucket__item"><svg viewBox="0 0 15 13"><path d="M1 7l4 4 9-10" fill="none" stroke="#c8a92e" stroke-width="3"/></svg>Have self-worth</li>
      <li class="bucket__item"><svg viewBox="0 0 15 13"><path d="M1 7l4 4 9-10" fill="none" stroke="#c8a92e" stroke-width="3"/></svg>Advocate for themselves</li>
      <li class="bucket__item"><svg viewBox="0 0 15 13"><path d="M1 7l4 4 9-10" fill="none" stroke="#c8a92e" stroke-width="3"/></svg>Feel secure in their future</li>
    </ul>
  </section>

  <section class="bucket bucket--social">
    <h2 class="bucket__title">Social</h2>
    <ul class="bucket__list">
      <li class="bucket__item"><svg viewBox="0 0 15 13"><path d="M1 7l4 4 9-10" fill="none" stroke="#c8a92e" stroke-width="3"/></svg>Embrace differences</li>
      <li class="bucket__item"><svg viewBox="0 0 15 13"><path d="M1 7l4 4 9-10" fill="none" stroke="#c8a92e" stroke-width="3"/></svg>Engage in trusting relationships</li>
      <li class="bucket__item"><svg viewBox="0 0 15 13"><path d="M1 7l4 4 9-10" fill="none" stroke="#c8a92e" stroke-width="3"/></svg>Be compassionate<span class="bucket__note">(members of their community)</span></li>
    </ul>
  </section>

  <section class="bucket bucket--academic">
    <h2 class="bucket__title">Academic</h2>
    <ul class="bucket__list">
      <li class="bucket__item"><svg viewBox="0 0 15 13"><path d="M1 7l4 4 9-10" fill="none" stroke="#c8a92e" stroke-width="3"/></svg>Apply skills and strategies</li>
      <li class="bucket__item"><svg viewBox="0 0 15 13"><path d="M1 7l4 4 9-10" fill="none" stroke="#c8a92e" stroke-width="3"/></svg>Creatively problem-solve</li>
      <li class="bucket__item"><svg viewBox="0 0 15 13"><path d="M1 7l4 4 9-10" fill="none" stroke="#c8a92e" stroke-width="3"/></svg>Achieve individual success</li>
    </ul>
  </section>

  <div class="sheet__footer-strip"></div>
  <div class="sheet__band-bottom"></div>
</main>
</body>
</html>
```